Flyer Design / Authenticity Certificate - Art Work

Looking for a design of a "Authenticity Certificate" - flyer, that will include some basic company info like logo etc, and allow our in house artist to sign and authenticate before it is applied the reverse of one of the paintings we will sell. Linked with our online sales website - "Amber Harbor Studios", where we recreate one off oil paintings from digital photographs. Our business logo should be incorporated in the design, along with a section for "Artisit Name" "Artisit Signature" "Ref Code"
Updates

Hi.. Sorry I should have added the size we need - please design accordingly to A6. Thanks.

Industry/Entity Type

It Company

Font styles to use
Serif
Script

Colors

Designer to choose colors to be used in the design.

Requirements
Must have
• Company logo
• Area for artist to print and sign
• Area for a reference
Nice to have
• must use the logo, maybe incorporate a "seal" icon, like what was used as a wax seal on older style documents

```html
<!DOCTYPE html>
<html lang="en">
<head>
<meta charset="utf-8">
<title>Certificate of Authenticity – Amber Harbor Studios</title>
<link rel="stylesheet" href="https://fonts.googleapis.com/css2?family=Cinzel:wght@400&family=Great+Vibes&family=Montserrat:wght@500&family=Open+Sans:wght@400&family=Arimo:wght@700&display=swap">
<style>
  :root {
    --panel-grey: #9d9ea2;
    --band-dark: #48484b;
    --band-red: #b3152f;
    --band-orange: #f39a1e;
    --paper: #e8f4f3;
    --paper-light: #f3faf9;
    --ink: #141a2a;
    --script-red: #9c1a31;
    --logo-light: #e4e4e6;
    --logo-ring: #3f3f42;
    --frame: #454547;
    --muted: #3b3d42;
  }
  * { margin: 0; padding: 0; box-sizing: border-box; }
  html, body { width: 1200px; height: 851px; overflow: hidden; background: #fff; }
  .certificate {
    position: relative;
    width: 1200px;
    height: 851px;
    overflow: hidden;
    background: linear-gradient(160deg, var(--paper-light), var(--paper));
    font-family: "Open Sans", Arial, sans-serif;
    color: var(--ink);
  }
  .certificate__bands { position: absolute; inset: 0; }

  .brand {
    position: absolute;
    left: 0;
    top: 32px;
    width: 506px;
    text-align: center;
  }
  .brand__mark {
    display: block;
    width: 136px;
    height: 136px;
    margin: 0 auto;
    border-radius: 50%;
    background: var(--logo-ring);
  }
  .brand__name {
    margin-top: 20px;
    font-family: "Montserrat", Arial, sans-serif;
    font-weight: 500;
    color: var(--logo-light);
    letter-spacing: 3px;
    line-height: 1;
  }
  .brand__name-main { display: block; font-size: 33px; }
  .brand__name-sub { display: block; font-size: 13px; letter-spacing: 10px; margin-top: 8px; }

  .artwork-frame {
    position: absolute;
    left: 78px;
    top: 276px;
    width: 349px;
    height: 518px;
    background: var(--frame);
    padding: 8px 9px 9px 9px;
  }
  .artwork {
    position: relative;
    width: 100%;
    height: 100%;
    background:
      radial-gradient(ellipse at 50% 55%, #b0452f 0%, rgba(176,69,47,0) 45%),
      linear-gradient(180deg, #e9e4e8 0%, #c9d5e2 30%, #d8b06a 60%, #e9c948 80%, #e7dcc9 100%);
  }
  .artwork__label {
    position: absolute;
    left: 0;
    right: 0;
    text-align: center;
    font-family: "Arimo", Arial, sans-serif;
    font-weight: 700;
    font-size: 37px;
    line-height: 46px;
    color: #000;
  }
  .artwork__label--top { top: 8px; }
  .artwork__label--bottom { top: 360px; }

  .title {
    position: absolute;
    left: 520px;
    width: 680px;
    text-align: center;
    font-family: "Cinzel", Georgia, serif;
    font-weight: 400;
    color: var(--ink);
  }
  .title__main { top: 42px; font-size: 87px; line-height: 1; letter-spacing: 1px; }
  .title__sub { top: 128px; font-size: 46px; line-height: 1; }
  .statement {
    position: absolute;
    left: 520px;
    width: 680px;
    top: 200px;
    text-align: center;
    font-size: 18px;
    color: var(--ink);
  }
  .artist-name {
    position: absolute;
    left: 520px;
    width: 680px;
    top: 300px;
    text-align: center;
    font-family: "Great Vibes", cursive;
    font-size: 138px;
    line-height: 1;
    color: var(--script-red);
  }
  .signature {
    position: absolute;
    left: 546px;
    top: 662px;
    width: 304px;
  }
  .signature__line { height: 3px; background: var(--script-red); }
  .signature__label {
    margin-top: 10px;
    text-align: center;
    font-size: 18px;
    color: var(--ink);
  }
  .reference {
    position: absolute;
    left: 546px;
    top: 782px;
    font-size: 19px;
    line-height: 25px;
  }
  .reference__label { color: var(--ink); }
  .reference__code { color: var(--muted); }
  .seal {
    position: absolute;
    left: 906px;
    top: 572px;
    width: 242px;
    height: 242px;
    border-radius: 50%;
    background: radial-gradient(circle at 40% 35%, #f7d77c 0%, #d9a23a 45%, #a86a14 85%, #7d4b0c 100%);
  }
</style>
</head>
<body>
<main class="certificate">
  <svg class="certificate__bands" width="1200" height="851" viewBox="0 0 1200 851" aria-hidden="true">
    <polygon points="482,0 512,0 514,851 506,851" fill="var(--band-orange)"/>
    <polygon points="480,0 486,0 514,851 478,851" fill="var(--band-red)"/>
    <polygon points="474,0 482,0 480,851 450,851" fill="var(--band-dark)"/>
    <polygon points="0,0 476,0 452,851 0,851" fill="var(--panel-grey)"/>
  </svg>

  <header class="brand">
    <span class="brand__mark"></span>
    <p class="brand__name">
      <span class="brand__name-main">AMBER HARBOR</span>
      <span class="brand__name-sub">STUDIOS</span>
    </p>
  </header>

  <figure class="artwork-frame">
    <div class="artwork" role="img" aria-label="Colourful oil painting of a stag's head with dripping paint">
      <p class="artwork__label artwork__label--top">SAMPLE<br>ARTWORK<br>ONLY</p>
      <p class="artwork__label artwork__label--bottom">SAMPLE<br>ARTWORK<br>ONLY</p>
    </div>
  </figure>

  <h1 class="title title__main">CERTIFICATE</h1>
  <p class="title title__sub">Of Authenticity</p>
  <p class="statement">THIS IS TO CERTIFY THAT THIS ARTWORK IS AUTHENTIC</p>

  <p class="artist-name">Artist Name</p>

  <div class="signature">
    <div class="signature__line"></div>
    <p class="signature__label">ARTIST SIGNATURE</p>
  </div>

  <div class="reference">
    <p class="reference__label">REFERENCE CODE:</p>
    <p class="reference__code">ABC-1234-XXX</p>
  </div>

  <div class="seal" role="img" aria-label="Gold wax seal"></div>
</main>
</body>
</html>
```